Consulting firm needs a professional letterhead design

We need a professional letterhead design which is simple but unique. It should carry attributes of the latest designs in the market suitable for professional environmental consultancies.

- The logo is attached for you to USE.
- Our preferred color scheme is that shown in the logo.
- Letterhead text color is your choice to make.
- Logo to the left and text to the right plus slogan/tagline is desirable for this letterhead.

Use any address etc. of your choice in the letterhead.

Target Market(s)

Consulting firms and government agencies

Industry/Entity Type

Environmental Consultant

Colors
acd037
fece3e
85cae6
3277b5

Requirements
Must have
• Logo supplied and color scheme must be used.
Nice to have
• Nexa font is used in the Logo, so it would ne nice to have nexa font in the letterhead too.

```html
<!DOCTYPE html>
<html lang="en">
<head>
<meta charset="utf-8">
<title>Terravant Letterhead</title>
<link rel="stylesheet" href="https://fonts.googleapis.com/css2?family=Open+Sans:wght@400;600&family=Roboto:wght@400&display=swap">
<style>
  :root {
    --backdrop: #dcdcdc;
    --paper: #fafafa;
    --ink: #5a5a5a;
    --brand-slate: #4f5168;
    --brand-blue: #5b9fbd;
    --brand-green: #8cbf45;
    --icon-blue: #4f8fb5;
    --signature-tone: #e6e6e6;
  }
  * { box-sizing: border-box; margin: 0; padding: 0; }
  html, body { width: 1200px; height: 800px; overflow: hidden; }
  body {
    background: var(--backdrop);
    font-family: "Open Sans", sans-serif;
    color: var(--ink);
    position: relative;
  }
  .letterhead {
    position: absolute;
    left: 330px; top: 23px;
    width: 540px; height: 754px;
    background: var(--paper);
  }
  .brand {
    position: absolute;
    left: 48px; top: 66px;
    display: flex; align-items: center; gap: 8px;
  }
  .brand-dot {
    width: 14px; height: 14px; border-radius: 50%;
    background: var(--brand-green);
  }
  .brand-text { line-height: 1; }
  .brand-name {
    font-size: 20px; font-weight: 600; letter-spacing: 1px;
    color: var(--brand-slate);
  }
  .brand-tagline {
    font-size: 7px; font-weight: 600;
    color: var(--brand-slate); margin-top: 2px;
  }
  .contact {
    position: absolute;
    left: 358px; top: 63px;
    border-left: 1px solid var(--brand-green);
    padding-left: 13px;
    font-family: "Roboto", sans-serif;
    font-size: 9.5px; line-height: 12.5px;
    color: var(--ink);
    list-style: none;
  }
  .contact li { display: flex; align-items: center; gap: 3px; }
  .contact svg { width: 8px; height: 8px; fill: var(--icon-blue); }
  .letter-body {
    position: absolute;
    left: 48px; top: 168px; width: 438px;
    font-size: 10px; line-height: 14.6px;
    text-align: justify;
  }
  .letter-body p { margin-bottom: 14.6px; }
  .signature {
    display: block;
    width: 64px; height: 60px;
    background: var(--signature-tone);
    border-radius: 4px;
  }
  .footer-band {
    position: absolute;
    left: 0; top: 705px;
    width: 457px; height: 23px;
    background: var(--brand-slate);
    color: #fff;
    font-family: "Roboto", sans-serif;
    font-size: 10px;
    display: flex; align-items: center; justify-content: center;
  }
  .footer-accent {
    position: absolute;
    left: 497px; top: 705px;
    width: 37px; height: 23px;
    background: linear-gradient(90deg, var(--brand-blue), #6aaec4);
  }
</style>
</head>
<body>
  <main class="letterhead">
    <header class="brand">
      <span class="brand-dot"></span>
      <div class="brand-text">
        <div class="brand-name">TERRAVANT</div>
        <div class="brand-tagline">Connecting research and sound policy</div>
      </div>
    </header>

    <ul class="contact">
      <li><svg viewBox="0 0 10 10"><path d="M1 3c0-1 1-2 4-2s4 1 4 2v1H7V3H3v1H1zM2 5h6l1 4H1z"/></svg>555.204.7180</li>
      <li><svg viewBox="0 0 10 10"><path d="M0 2h10v6H0zM1 3l4 3 4-3" stroke="#fff" stroke-width=".8"/></svg>info@yourmail.com</li>
      <li><svg viewBox="0 0 10 10"><circle cx="5" cy="5" r="5"/><path d="M2 4c1-1 2 0 3 1s0 2 1 3M6 1c0 2 2 2 3 2" stroke="#fff" stroke-width=".8" fill="none"/></svg>www.yourwebsite.com</li>
    </ul>

    <section class="letter-body">
      <p>Dear customer,</p>
      <p>Lorem ipsum dolor sit amet, consectetur adipisicing elit, sed do eiusmod tempor incididunt ut labore et dolore magna aliqua. Ut enim ad minim veniam, quis nostrud exercitation ullamco laboris nisi ut aliquip ex ea commodo consequat. Duis aute irure dolor in reprehenderit in voluptate velit esse cillum dolore eu fugiat nulla pariatur. Excepteur sint occaecat cupidatat non proident, sunt in culpa qui officia deserunt mollit anim id est laborum.</p>
      <p>Lorem ipsum dolor sit amet, consectetur adipisicing elit, sed do eiusmod tempor incididunt ut labore et dolore magna aliqua. Ut enim ad minim veniam, quis nostrud exercitation ullamco laboris nisi ut aliquip ex ea commodo consequat. Duis aute irure dolor in reprehenderit in voluptate velit esse cillum dolore eu fugiat nulla pariatur. Excepteur sint occaecat cupidatat non proident, sunt in culpa qui officia deserunt mollit anim id est laborum.</p>
      <p>Lorem ipsum dolor sit amet, consectetur adipisicing elit, sed do eiusmod tempor incididunt ut labore et dolore magna aliqua. Ut enim ad minim veniam, quis nostrud exercitation ullamco laboris nisi ut aliquip ex ea commodo consequat. Duis aute irure dolor in reprehenderit in voluptate velit esse cillum dolore eu fugiat nulla pariatur. Excepteur sint occaecat cupidatat non proident, sunt in culpa qui officia deserunt mollit anim id est laborum.</p>
      <p>Lorem ipsum dolor sit amet, consectetur adipisicing elit, sed do eiusmod tempor incididunt ut labore et dolore magna aliqua. Ut enim ad minim veniam, quis nostrud exercitation ullamco laboris nisi ut aliquip ex ea commodo consequat. Duis aute irure dolor in reprehenderit.</p>
      <p>Yours Sincerely,</p>
      <span class="signature" role="img" aria-label="Handwritten signature of the sender"></span>
    </section>

    <footer class="footer-band">1820 Harbor Crest Drive, Suite 210 Bayview.</footer>
    <div class="footer-accent"></div>
  </main>
</body>
</html>
```